Italian Restaurant Responsive Wordpress Website Design

Italian Restaurant is looking to create a new responsive website design based on some Wordpress templates that have been selected as favourites. We want to base the influence of the design off a business card that was recently created (attached below).
The design should be based of these templates that will be purchased when selected. All templates are responsive. Please read details of templates to learn more about their functions and features. After we select the designs we can deliver the customizable PSD files.
http://layoutmarket.example/item/tavola-responsive-restaurant-wordpress-theme/full_screen_preview/7316428
http://pelmodesigns.example/themes/?theme=Caldora
http://themes.brightwexel.example/fettora/
http://www.tablekitlayouts.example/
Pages required
Homepage
-Navigation
-Contact info always accessible on all responsive viewports. You may have to include a design for Contact info on mobile viewport to the top of the page.
-Hours of Operation
About Page
Menu
-Styling of content will be very identical to menu's. That will be provided once I receive a copy.
Gallery
Contact Page
-Show a map, Contact Details and a Contact/Feedback Form
We are open to any designs that you want to lay on top of these Template designs. The current site is: www.quartolume.example If you want an indication of content.
Any questions please ask! Enjoy!
Updates
Hello Everyone. I just updated the menu being used in the restaurant as well as the fonts that are being used as we speak. Any questions please email me. Cheers.
Target Market(s)
The Target Market is families and a more distinguished crowd. They offer valued gourmet food but are located in a very high end neighbourhood. Want to deliver home made cuisine that's approachable but yet considered gourmet.
Industry/Entity Type
Business
Look and feel
Each slider illustrates characteristics of the customer's brand and the style your logo design should communicate.

```html
<!DOCTYPE html>
<html lang="en">
<head>
<meta charset="utf-8">
<title>Quarto Lume — Contact Us</title>
<link href="https://fonts.googleapis.com/css2?family=Lato:wght@400;700&family=Lobster+Two:ital,wght@1,700&display=swap" rel="stylesheet">
<style>
:root{
  --header-bg:#f3f0ea;
  --ink:#2f2a27;
  --nav-ink:#3a3430;
  --brand-red:#a63a28;
  --accent:#e8472f;
  --accent-dark:#cf3a24;
  --muted:#a8a6a3;
  --label:#6e6a66;
  --field-bg:#f7f7f7;
  --field-line:#d8d6d3;
  --footer-bg:#3d3531;
  --footer-field:#575049;
  --footer-ink:#f1ece6;
  --map-tone:#e7e2d4;
}
*{box-sizing:border-box;margin:0;padding:0}
html,body{width:1130px;height:1200px;overflow:hidden;background:#fff}
body{position:relative;font-family:'Lato',sans-serif;color:var(--ink)}

.hero{position:absolute;left:0;top:0;width:1130px;height:238px;
  background:linear-gradient(100deg,#e9d9cf 0%,#f1e3da 25%,#ece6dc 50%,#e6e3d3 70%,#efddd2 100%)}
.site-header{position:absolute;left:0;top:0;width:1130px;height:71px;background:var(--header-bg);
  box-shadow:0 1px 3px rgba(0,0,0,.18)}
.main-nav a{position:absolute;top:41px;font-weight:700;font-size:14px;color:var(--nav-ink);text-decoration:none;letter-spacing:.1px}
.main-nav a.is-current{color:var(--brand-red)}
.brand{position:absolute;left:465px;top:22px;width:200px;text-align:center;
  font-weight:700;font-size:24px;color:var(--brand-red)}
.brand-dot{position:absolute;left:557px;top:6px;width:16px;height:16px;border-radius:50%;background:var(--brand-red)}

.page-title{position:absolute;left:131px;top:168px;width:869px;height:70px;background:rgba(245,241,234,.78);padding:13px 22px}
.page-title h1{font-weight:400;font-size:19px;color:var(--ink)}
.page-title p{font-size:13.5px;color:var(--ink);margin-top:1px}

.map{position:absolute;left:149px;top:269px;width:831px;height:353px;background:var(--map-tone)}

.section-title{position:absolute;top:657px;font-weight:700;font-size:14px;color:var(--ink);letter-spacing:.2px}
.field-label{position:absolute;font-size:12px;color:var(--label)}
.field-label span{color:var(--muted)}
.field{position:absolute;background:var(--field-bg);border:1px solid var(--field-line);border-radius:3px}
.btn{position:absolute;display:flex;align-items:center;justify-content:center;border-radius:2px;
  background:linear-gradient(var(--accent),var(--accent-dark));color:#fff;
  font-family:'Lobster Two',cursive;font-style:italic;font-weight:700;font-size:16px}

.contact-info{position:absolute;left:790px;top:709px;font-size:13px;line-height:17.6px;color:var(--ink)}
.contact-info address{font-style:normal;margin-bottom:17px}
.contact-info dt{display:inline;font-weight:700}
.contact-info dd{display:inline;color:#555}
.contact-info dd::after{content:"";display:block}

.site-footer{position:absolute;left:0;top:1028px;width:1130px;height:172px;background:var(--footer-bg);color:var(--footer-ink)}
.newsletter h2{position:absolute;left:149px;top:27px;font-weight:400;font-size:14px;letter-spacing:.5px}
.newsletter p{position:absolute;left:149px;top:46px;font-size:13px;letter-spacing:.2px}
.newsletter .email{position:absolute;left:450px;top:26px;width:310px;height:37px;background:var(--footer-field);
  border-radius:2px;padding:10px 18px;font-size:13px;font-style:italic;color:#958c84}
.footer-rule{position:absolute;left:110px;top:89px;width:910px;height:1px;background:rgba(0,0,0,.35);box-shadow:0 1px 0 rgba(255,255,255,.05)}
.legal{position:absolute;left:0;top:113px;width:1130px;text-align:center;font-size:12px;line-height:15px}
</style>
</head>
<body>

<div class="hero" role="img" aria-label="Soft-focus photograph of fresh tomatoes, basil and mozzarella"></div>

<header class="site-header">
  <nav class="main-nav">
    <a href="#" style="left:149px">HOME</a>
    <a href="#" style="left:246px">MENUS</a>
    <a href="#" class="is-current" style="left:349px">ABOUT US</a>
    <a href="#" style="left:691px">GROUPS</a>
    <a href="#" style="left:802px">VIP LIST</a>
    <a href="#" style="left:909px">CONTACT</a>
  </nav>
  <span class="brand-dot"></span>
  <div class="brand">Quarto Lume</div>
</header>

<section class="page-title">
  <h1>Contact Us</h1>
  <p>Lorem ipsum dolor sit amet, consectetuer adipiscing elit.</p>
</section>

<div class="map" role="img" aria-label="Street map showing the restaurant's neighbourhood"></div>

<h2 class="section-title" style="left:151px">LEAVE US A MESSAGE</h2>
<form>
  <label class="field-label" style="left:150px;top:709px">Name <span>(required)</span></label>
  <div class="field" style="left:150px;top:731px;width:198px;height:33px"></div>
  <label class="field-label" style="left:362px;top:709px">Email <span>(required)</span></label>
  <div class="field" style="left:360px;top:731px;width:198px;height:33px"></div>
  <label class="field-label" style="left:574px;top:709px">Subject <span>(required)</span></label>
  <div class="field" style="left:569px;top:731px;width:198px;height:33px"></div>
  <label class="field-label" style="left:150px;top:785px">Your Message <span>(required)</span></label>
  <div class="field" style="left:150px;top:807px;width:618px;height:132px"></div>
  <div class="btn" style="left:646px;top:951px;width:122px;height:34px">Submit</div>
</form>

<h2 class="section-title" style="left:790px">CONTACT INFO</h2>
<div class="contact-info">
  <address>48 Harlow Park Lane<br>Brookvale, CA 94021<br>USA</address>
  <dl>
    <dt>Phone:</dt> <dd>(123) 456-7890</dd>
    <dt>Fax:</dt> <dd>+08 (123) 456-7890</dd>
    <dt>Email:</dt> <dd>info@quartolume.example</dd>
    <dt>Web:</dt> <dd>quartolume.example</dd>
  </dl>
</div>

<footer class="site-footer">
  <div class="newsletter">
    <h2>SIGN UP FOR OUR NEWSLETTER</h2>
    <p>and recieve notifications from us</p>
    <div class="email">enter your email</div>
    <div class="btn" style="left:781px;top:26px;width:172px;height:37px">Signup Today</div>
  </div>
  <div class="footer-rule"></div>
  <p class="legal">Quarto Lume 212 Marlowe Ave. W. Toronto, ON (555) 014-0188<br>Copyright © 2013 TableNorth</p>
</footer>

</body>
</html>
```